Grace Fellowship Ardmore, MS needs a Business Card design

We are in the process of rebranding our church with a new logo with a fresh appeal to younger families moving into our community and joining our church. We are in need of a new business card design and would like to see 2 sided designs that incorporate the web color 00cccc.

We would like to have our logo, church name (grace fellowship ardmore) and our what we are about (gather.grow.serve.) in addition to the following information:
Name: Dr. Samuel Whitfield
Title: Teaching Pastor
Phone: 5555550142
Email: swhitfield@gfcardmore.example
Website: www.gfcardmore.example
Address: 714 N Elmwood Avenue Ardmore, XZ 39187

Target Market(s)

Ardmore, XZ is a bedroom community outside of Jackson that is experiencing exponential growth with young professionals/young families moving in. We are making a lot of changes to reach this demographic while still honoring and continuing to reach those who have lived here for a while.

Industry/Entity Type

Church

Contact Information for Business Card

Grace Fellowship Ardmore - gather.grow.serve.
Dr. Samuel Whitfield
Teaching Pastor
5555550142
swhitfield@gfcardmore.example
www.gfcardmore.example
714 N Elmwood Avenue
Ardmore, XZ 39187

Font styles to use
Sans Serif

```html
<!DOCTYPE html>
<html lang="en">
<head>
<meta charset="utf-8">
<title>Grace Fellowship Ardmore – Business Card</title>
<link href="https://fonts.googleapis.com/css2?family=Barlow:wght@400;500;600&display=swap" rel="stylesheet">
<style>
  :root {
    --card-mint: #57ffbe;
    --ink-slate: #5d6a72;
    --paper-white: #ffffff;
    --tab-white: #eefcf6;
    --rule-line: #3fcf97;
  }
  * { margin: 0; padding: 0; box-sizing: border-box; }
  html, body { width: 1200px; height: 1200px; overflow: hidden; background: var(--paper-white); }
  body { position: relative; font-family: "Barlow", sans-serif; }

  .card { position: absolute; background: var(--card-mint); width: 886px; height: 540px; }
  .card-front { left: 157px; top: 21px; }
  .card-back { left: 154px; top: 624px; }

  /* Front */
  .front-mark { position: absolute; left: 373px; top: 150px; width: 140px; height: 140px; border-radius: 50%; background: var(--paper-white); }
  .front-name { position: absolute; left: 0; right: 0; top: 344px; text-align: center; font-size: 31px; font-weight: 500; letter-spacing: 1px; color: var(--ink-slate); text-transform: uppercase; }
  .front-tagline { position: absolute; left: 0; right: 0; top: 395px; text-align: center; font-size: 19px; letter-spacing: 1.5px; color: var(--ink-slate); }

  /* Back */
  .side-rule { position: absolute; left: 67px; top: 0; width: 2px; height: 100%; background: var(--rule-line); }
  .icon-tab { position: absolute; left: 0; width: 68px; background: var(--tab-white); display: flex; align-items: center; justify-content: center; border-bottom: 1px solid #cfe9de; }
  .icon-tab svg { fill: var(--ink-slate); }
  .tab-person { top: 84px; height: 69px; }
  .holder-name { position: absolute; left: 84px; top: 88px; font-size: 37px; font-weight: 600; color: var(--paper-white); letter-spacing: 0.5px; }
  .holder-title { position: absolute; left: 85px; top: 134px; font-size: 22px; color: var(--paper-white); letter-spacing: 1px; }

  .contact-row { position: absolute; left: 84px; font-size: 21px; color: var(--paper-white); letter-spacing: 1px; border-bottom: 1px solid rgba(255,255,255,0.6); height: 36px; line-height: 36px; width: 318px; white-space: nowrap; }
  .contact-row.wide { width: 440px; }

  .back-mark { position: absolute; left: 700px; top: 108px; width: 68px; height: 68px; border-radius: 50%; background: var(--paper-white); }
  .back-name { position: absolute; left: 600px; width: 270px; top: 210px; text-align: center; font-size: 18px; color: var(--paper-white); text-transform: uppercase; letter-spacing: 0.5px; }
  .back-tagline { position: absolute; left: 600px; width: 270px; top: 234px; text-align: center; font-size: 13px; color: var(--paper-white); letter-spacing: 1px; }
</style>
</head>
<body>
  <section class="card card-front">
    <div class="front-mark"></div>
    <div class="front-name">Grace Fellowship Ardmore</div>
    <div class="front-tagline">gather. grow. serve.</div>
  </section>

  <section class="card card-back">
    <div class="side-rule"></div>

    <div class="icon-tab tab-person">
      <svg width="40" height="40" viewBox="0 0 40 40"><circle cx="20" cy="12" r="8"/><path d="M4 38 C4 26 10 22 20 22 C30 22 36 26 36 38 Z"/></svg>
    </div>
    <div class="holder-name">Dr. Samuel Whitfield</div>
    <div class="holder-title">Teaching Pastor</div>

    <div class="icon-tab" style="top:274px;height:34px">
      <svg width="20" height="20" viewBox="0 0 24 24"><path d="M6.6 10.8a15 15 0 0 0 6.6 6.6l2.2-2.2c.3-.3.7-.4 1-.2 1.1.4 2.3.6 3.6.6.6 0 1 .4 1 1V20c0 .6-.4 1-1 1A17 17 0 0 1 3 4c0-.6.4-1 1-1h3.5c.6 0 1 .4 1 1 0 1.3.2 2.5.6 3.6.1.3 0 .7-.2 1z"/></svg>
    </div>
    <div class="contact-row" style="top:272px">5555550142</div>

    <div class="icon-tab" style="top:308px;height:38px">
      <svg width="18" height="14" viewBox="0 0 24 18"><path d="M0 0h24v3L12 10 0 3z"/><path d="M0 6l12 7 12-7v12H0z"/></svg>
    </div>
    <div class="contact-row" style="top:308px">swhitfield@gfcardmore.example</div>

    <div class="icon-tab" style="top:346px;height:35px">
      <svg width="20" height="20" viewBox="0 0 24 24"><circle cx="12" cy="12" r="10"/><path d="M2 12h20M12 2v20M5 6h14M5 18h14" stroke="#eefcf6" stroke-width="1.4" fill="none"/><ellipse cx="12" cy="12" rx="4.5" ry="10" stroke="#eefcf6" stroke-width="1.4" fill="none"/></svg>
    </div>
    <div class="contact-row" style="top:345px">www.gfcardmore.example</div>

    <div class="icon-tab" style="top:381px;height:40px">
      <svg width="16" height="22" viewBox="0 0 16 22"><path d="M8 0a8 8 0 0 0-8 8c0 6 8 14 8 14s8-8 8-14a8 8 0 0 0-8-8zm0 11a3 3 0 1 1 0-6 3 3 0 0 1 0 6z"/></svg>
    </div>
    <div class="contact-row wide" style="top:382px">714 N Elmwood Avenue Ardmore, XZ 39187</div>

    <div class="back-mark"></div>
    <div class="back-name">Grace Fellowship Ardmore</div>
    <div class="back-tagline">gather. grow. serve.</div>
  </section>
</body>
</html>
```